Letterhead and envelope design

Using current logo and colours I would like to have a new design done for a stationary set to be printed.

The new files should include logo, web and email address as well as,mailing address and phone number

Dov Harmsby
Harmsby Construction Inc
Box 27 Site 18 RR5
Okotoks AB
T4K 2B9
Cell : 403-555-2917
Email: dov@harmsbyconstruction.example
web: harmsbyconstruction.example

```html
<!DOCTYPE html>
<html lang="en">
<head>
<meta charset="utf-8">
<title>Harmsby Construction Letterhead</title>
<link href="https://fonts.googleapis.com/css2?family=Roboto:wght@400;500&display=swap" rel="stylesheet">
<style>
  :root {
    --navy: #00356b;
    --orange: #e8971e;
    --ink: #333333;
    --paper: #ffffff;
    --backdrop: #716c6c;
    --sig-tone: #e6e6e6;
  }
  * { margin: 0; padding: 0; box-sizing: border-box; }
  html, body {
    width: 873px; height: 1200px; overflow: hidden;
    background: var(--backdrop);
    font-family: "Roboto", Arial, sans-serif;
  }
  .letterhead {
    position: absolute; left: 27.5px; top: 26.5px;
    width: 816px; height: 1154px;
    background: var(--paper);
    box-shadow: 0 0 6px rgba(0,0,0,.35);
  }
  .rule {
    position: absolute; height: 3px; background: var(--orange);
  }
  .rule--head-left { left: 0; width: 72px; top: 91.5px; }
  .rule--head-right { left: 222px; right: 0; top: 91.5px; }
  .rule--foot { left: 0; right: 0; top: 1069px; }
  .brand-disc {
    position: absolute; left: 74px; top: 22px;
    width: 146px; height: 146px; border-radius: 50%;
    background: var(--navy);
  }
  .brand-name {
    position: absolute; left: 238px; top: 52px;
    font-size: 36px; font-weight: 500; line-height: 1;
    color: var(--navy); letter-spacing: -0.3px;
    white-space: nowrap;
  }
  .letter-date {
    position: absolute; right: 75px; top: 227px;
    font-size: 17px; color: var(--ink);
  }
  .letter-body {
    position: absolute; left: 75.5px; width: 664.5px; top: 267px;
    color: var(--ink);
  }
  .salutation { font-size: 18px; margin-bottom: 18px; }
  .letter-body p {
    font-size: 16px; line-height: 23.3px;
    text-align: justify; margin-bottom: 23.5px;
  }
  .closing { font-size: 18px; margin-top: 26px; }
  .signature-area {
    position: absolute; left: 68px; top: 845px;
    width: 134px; height: 58px; border-radius: 6px;
    background: linear-gradient(90deg, var(--sig-tone), #f3f3f3);
  }
  .contact {
    position: absolute; top: 1045px;
    display: flex; flex-direction: column; align-items: center;
    transform: translateX(-50%);
  }
  .contact-icon {
    width: 46px; height: 46px; border-radius: 50%;
    background: var(--navy); border: 3px solid var(--orange);
    display: flex; align-items: center; justify-content: center;
  }
  .contact-icon svg { width: 24px; height: 24px; fill: #fff; }
  .contact-text {
    margin-top: 18px; font-size: 15px; font-weight: 500;
    color: var(--ink); text-align: center; line-height: 19.5px;
    white-space: nowrap;
  }
  .contact--address { left: 95px; }
  .contact--web { left: 298px; }
  .contact--phone { left: 501px; }
  .contact--email { left: 690px; }
</style>
</head>
<body>
<main class="letterhead">
  <div class="rule rule--head-left"></div>
  <div class="rule rule--head-right"></div>
  <div class="brand-disc"></div>
  <div class="brand-name">HARMSBY CONSTRUCTION</div>

  <div class="letter-date">XX-XX-XXXX</div>

  <section class="letter-body">
    <div class="salutation">Dear Clients</div>
    <p>Lorem ipsum dolor sit amet, consectetur adipiscing elit, sed do eiusmod tempor incididunt ut labore et dolore magna aliqua. Ut enim ad minim veniam, quis nostrud exercitation ullamco laboris nisi ut aliquip ex ea commodo consequat. Duis aute irure dolor in reprehenderit in voluptate velit esse cillum dolore eu fugiat nulla pariatur. Excepteur sint occaecat cupidatat non proident, sunt in culpa qui officia deserunt mollit anim id est laborum.</p>
    <p>Lorem ipsum dolor sit amet, consectetur adipiscing elit, sed do eiusmod tempor incididunt ut labore et dolore magna aliqua. Ut enim ad minim veniam, quis nostrud exercitation ullamco laboris nisi ut aliquip ex ea commodo consequat. Duis aute irure dolor in reprehenderit in voluptate velit esse cillum dolore eu fugiat nulla pariatur. Excepteur sint occaecat cupidatat non proident, sunt in culpa qui officia deserunt mollit anim id est laborum.</p>
    <p>Lorem ipsum dolor sit amet, consectetur adipiscing elit, sed do eiusmod tempor incididunt ut labore et dolore magna aliqua. Ut enim ad minim veniam, quis nostrud exercitation ullamco laboris nisi ut aliquip ex ea commodo consequat. Duis aute irure dolor in reprehenderit in voluptate velit esse cillum dolore eu fugiat nulla pariatur. Excepteur sint occaecat cupidatat non proident, sunt in culpa qui officia deserunt mollit anim id est laborum.</p>
    <div class="closing">Sincerly,</div>
  </section>

  <div class="signature-area" role="img" aria-label="Handwritten signature"></div>

  <div class="rule rule--foot"></div>

  <div class="contact contact--address">
    <div class="contact-icon">
      <svg viewBox="0 0 24 24"><path d="M12 2a7 7 0 0 0-7 7c0 5 7 13 7 13s7-8 7-13a7 7 0 0 0-7-7zm0 9.5A2.5 2.5 0 1 1 12 6.5a2.5 2.5 0 0 1 0 5z"/></svg>
    </div>
    <div class="contact-text">Box 27 Site 18 RR5<br>Okotoks AB T4K 2B9</div>
  </div>

  <div class="contact contact--web">
    <div class="contact-icon">
      <svg viewBox="0 0 24 24"><path d="M12 2a10 10 0 1 0 0 20 10 10 0 0 0 0-20zm6.9 6h-3a15 15 0 0 0-1.3-3.9A8 8 0 0 1 18.9 8zM12 4c.9 1.2 1.6 2.5 2 4h-4c.4-1.5 1.1-2.8 2-4zM4.3 14a8 8 0 0 1 0-4h3.4a16 16 0 0 0 0 4H4.3zm.8 2h3a15 15 0 0 0 1.3 3.9A8 8 0 0 1 5.1 16zm3-8h-3a8 8 0 0 1 4.3-3.9A15 15 0 0 0 8.1 8zM12 20c-.9-1.2-1.6-2.5-2-4h4c-.4 1.5-1.1 2.8-2 4zm2.3-6H9.7a14 14 0 0 1 0-4h4.6a14 14 0 0 1 0 4zm.3 5.9A15 15 0 0 0 15.9 16h3a8 8 0 0 1-4.3 3.9zm1.7-5.9a16 16 0 0 0 0-4h3.4a8 8 0 0 1 0 4h-3.4z"/></svg>
    </div>
    <div class="contact-text">www.harmsbyconstruction.example</div>
  </div>

  <div class="contact contact--phone">
    <div class="contact-icon">
      <svg viewBox="0 0 24 24"><path d="M6.6 10.8a15 15 0 0 0 6.6 6.6l2.2-2.2a1 1 0 0 1 1-.25 11.4 11.4 0 0 0 3.6.57 1 1 0 0 1 1 1V20a1 1 0 0 1-1 1A17 17 0 0 1 3 4a1 1 0 0 1 1-1h3.5a1 1 0 0 1 1 1c0 1.25.2 2.45.57 3.57a1 1 0 0 1-.25 1z"/></svg>
    </div>
    <div class="contact-text">403-555-2917</div>
  </div>

  <div class="contact contact--email">
    <div class="contact-icon">
      <svg viewBox="0 0 24 24"><path d="M3 5h18a1 1 0 0 1 1 1v1l-10 6L2 7V6a1 1 0 0 1 1-1zm-1 4.3 10 6 10-6V18a1 1 0 0 1-1 1H3a1 1 0 0 1-1-1z"/></svg>
    </div>
    <div class="contact-text">dov@harmsbyconstruction.example</div>
  </div>
</main>
</body>
</html>
```